Business Card Needed for Crafter of Pottery, Jewelry and Artwork

Calling all designers in search of an artistic challenge.

I need a new business card design for my pottery, jewelry and artwork business, Woven Glass and Tide, based in Vancouver BC.

I would like a card that is bright and inviting and preferably incorporates my logo and a sample of photos of my work while having a clean fresh look. The following contact details would preferably be included on the card as well:
• Helena Pikeworth
• Designer
• Phone: 604.555.0172
• Email: Designer@WovenGlassandTide.example
• Website: www.WovenGlassandTide.example
• Blog: www.ShapingHillside.example

The logo is attached in two color schemes in both Vector and Source formats. On past cards I’ve also included photos of my work. By including photos of the work the pieces are showcased and it catches people’s eye and prompts them to pick up the card and look at it more closely. For example, if I leave a stack in a coffee shop I want people to be drawn to the card, to pick it up and get a sense of the my product lines. Please feel free to pull photos of my work directly off of my website. If you need photos with higher pixels please let me know and I’ll email them directly to you. The website background is bffbda (191, 251, 218). I would like the business cards to match the feel of the website for consistency but the cards do not need to use the exact same colors. My website and current business card are predominantly turquoise shades. The background uses stripes provided by the website template. I don’t know the exact colors of the stripes.

My current business card is attached to show the use of photos in a design. Please note that I am not thrilled with my own design and am looking for variations and completely new designs. This example is not meant to be used as a template or starting point.

Here is some background surrounding my company:
WGT offers one of a kind jewelry, pottery, artwork and leather bags each designed with a twist. The pottery varies from rustic every day functional ware to raku artwork. The jewelry ranges from simple sterling every day pieces to multimedia pieces incorporating stone, metal, ceramics and fabric. The artwork is multimedia, typically acrylic paired with a natural element such as bark. All the bags are leather with reworked kimono fabric or patterned silk lining.

Feel free to check out my website to get a flavour for my work and the color scheme I've used on marketing materials so far. www.wovenglassandtide.example
Updates

Thank you to everyone who has submitted a design so far. I hope everyone has received some helpful feedback.

I'm going to post a survey to customers and friends asking for their votes. If you have new designs to submit please try to get them in by Saturday March 30 at noon so that I can include it in the survey launch.

Thank you

Target Market(s)

Females aged 25-65 interested in one of a kind functional pottery and jewelry.

Industry/Entity Type

Coffee Shop

Requirements
Must have
• Contact information, website, blog
Nice to have
• Logo, photos

```html
<!DOCTYPE html>
<html lang="en">
<head>
<meta charset="utf-8">
<title>Woven Glass and Tide Business Card</title>
<link rel="stylesheet" href="https://fonts.googleapis.com/css2?family=Kaushan+Script&family=Crimson+Text:wght@400;700&display=swap">
<style>
  :root {
    --page-bg: #e9ebee;
    --card-white: #ffffff;
    --teal: #1fa596;
    --teal-deep: #138b80;
    --navy: #2c2f66;
    --slate: #8e93a8;
    --mist: #c9d1e3;
    --ink: #23245a;
    --photo-warm: #b98a6a;
    --photo-cool: #5f8f8a;
    --photo-light: #e4e2de;
  }
  * { box-sizing: border-box; margin: 0; padding: 0; }
  html, body {
    width: 1200px;
    height: 861px;
    overflow: hidden;
    background: var(--page-bg);
  }
  .card-spread {
    position: absolute;
    inset: 0;
    display: flex;
    align-items: center;
    justify-content: center;
    gap: 30px;
  }
  .card {
    position: relative;
    width: 560px;
    height: 320px;
    background: var(--card-white);
    overflow: hidden;
    box-shadow: 0 6px 18px rgba(0, 0, 0, 0.18);
  }
  .card svg.card-art {
    position: absolute;
    inset: 0;
    width: 100%;
    height: 100%;
  }
  .brand {
    position: absolute;
    top: 26px;
    left: 0;
    right: 0;
    display: flex;
    align-items: center;
    justify-content: center;
    gap: 8px;
    font-family: "Crimson Text", Georgia, serif;
    font-weight: 700;
    font-size: 15px;
    color: var(--navy);
    letter-spacing: 0.5px;
  }
  .brand-dot {
    width: 14px;
    height: 14px;
    border-radius: 50%;
    background: var(--teal);
  }
  .holder-name {
    position: absolute;
    top: 78px;
    left: 0;
    right: 0;
    text-align: center;
    font-family: "Kaushan Script", cursive;
    font-size: 40px;
    line-height: 1;
    color: var(--teal);
  }
  .holder-role {
    position: absolute;
    top: 122px;
    left: 0;
    right: 0;
    padding-left: 40px;
    text-align: center;
    font-family: "Kaushan Script", cursive;
    font-size: 19px;
    color: var(--teal);
  }
  .contact-list {
    position: absolute;
    top: 170px;
    left: 0;
    right: 0;
    list-style: none;
    text-align: center;
    font-family: "Crimson Text", Georgia, serif;
    font-size: 14.5px;
    line-height: 22px;
    color: var(--ink);
  }
  .contact-list .label { font-weight: 700; }
</style>
</head>
<body>
<main class="card-spread">

  <section class="card card-front">
    <svg class="card-art" viewBox="0 0 560 320" xmlns="http://www.w3.org/2000/svg">
      <defs>
        <linearGradient id="work-tones" x1="0" y1="0" x2="1" y2="1">
          <stop offset="0" stop-color="#d9d4cf"/>
          <stop offset="0.35" stop-color="#b98a6a"/>
          <stop offset="0.6" stop-color="#5f8f8a"/>
          <stop offset="1" stop-color="#e4e2de"/>
        </linearGradient>
      </defs>
      <rect class="work-collage" width="560" height="320" fill="url(#work-tones)" role="img" aria-label="Collage of handmade work: pottery mugs, jewelry pendants, necklaces, a raku plate, leather bags and acrylic artwork"/>
      <g class="collage-grid" stroke="#ffffff" stroke-width="5">
        <line x1="-320" y1="0" x2="0" y2="320"/>
        <line x1="-230" y1="0" x2="90" y2="320"/>
        <line x1="-140" y1="0" x2="180" y2="320"/>
        <line x1="-50" y1="0" x2="270" y2="320"/>
        <line x1="40" y1="0" x2="360" y2="320"/>
        <line x1="130" y1="0" x2="450" y2="320"/>
        <line x1="220" y1="0" x2="540" y2="320"/>
        <line x1="310" y1="0" x2="630" y2="320"/>
        <line x1="400" y1="0" x2="720" y2="320"/>
        <line x1="490" y1="0" x2="810" y2="320"/>
        <line x1="0" y1="0" x2="-320" y2="320"/>
        <line x1="90" y1="0" x2="-230" y2="320"/>
        <line x1="180" y1="0" x2="-140" y2="320"/>
        <line x1="270" y1="0" x2="-50" y2="320"/>
        <line x1="360" y1="0" x2="40" y2="320"/>
        <line x1="450" y1="0" x2="130" y2="320"/>
        <line x1="540" y1="0" x2="220" y2="320"/>
        <line x1="630" y1="0" x2="310" y2="320"/>
        <line x1="720" y1="0" x2="400" y2="320"/>
        <line x1="810" y1="0" x2="490" y2="320"/>
      </g>
    </svg>
  </section>

  <section class="card card-back">
    <svg class="card-art" viewBox="0 0 560 320" xmlns="http://www.w3.org/2000/svg" aria-hidden="true">
      <polygon class="corner-mist" points="0,0 160,0 0,160" fill="#c9d1e3"/>
      <polygon class="corner-teal-top" points="395,0 560,0 560,170" fill="#1fa596"/>
      <polygon class="corner-teal-bottom" points="0,195 0,320 180,320 55,195" fill="#1fa596"/>
      <polygon class="corner-slate" points="560,200 560,320 440,320" fill="#8e93a8"/>
      <polygon class="accent-navy" points="155,0 185,0 170,14" fill="#2c2f66"/>
      <polygon class="accent-navy" points="0,135 28,165 0,190" fill="#2c2f66"/>
      <polygon class="accent-navy" points="560,170 560,205 540,188" fill="#2c2f66"/>
      <polygon class="accent-navy" points="405,320 435,320 420,304" fill="#2c2f66"/>
    </svg>
    <div class="brand"><span class="brand-dot"></span>Woven Glass and Tide</div>
    <h1 class="holder-name">Helena Pikeworth</h1>
    <p class="holder-role">Designer</p>
    <ul class="contact-list">
      <li><span class="label">Phone:</span> 604.555.0172</li>
      <li><span class="label">Email:</span> Designer@WovenGlassandTide.example</li>
      <li><span class="label">Website:</span> www.WovenGlassandTide.example</li>
      <li><span class="label">Blog:</span> www.ShapingHillside.example</li>
    </ul>
  </section>

</main>
</body>
</html>
```